pathology learning flashcard template graphic design .

Creative designs for 2 sides of the flashcards to include colorful sectioning and font sizes that will make it easy to use in studying.

```html
<!DOCTYPE html>
<html lang="en">
<head>
<meta charset="utf-8">
<title>Pathology Flashcard – Gastrointestinal Case 0001</title>
<link rel="stylesheet" href="https://fonts.googleapis.com/css2?family=Kanit:ital,wght@0,200;1,600;1,700&family=Mulish:ital,wght@0,400;0,700;1,300;1,400;1,600&family=Tinos:wght@700&display=swap">
<style>
  :root{
    --pink:#e8197b;
    --orange:#f26424;
    --accent:#f05a28;
    --navy:#131a34;
    --white:#ffffff;
    --paper:#ffffff;
  }
  *{margin:0;padding:0;box-sizing:border-box;}
  html,body{width:1200px;height:436px;overflow:hidden;background:var(--paper);}
  .canvas{position:relative;width:1200px;height:436px;overflow:hidden;}
  .shapes{position:absolute;inset:0;}
  .txt{position:absolute;color:var(--white);white-space:nowrap;}

  /* Front card */
  .front-title{left:280px;top:84px;font:italic 700 24px/1 "Kanit",sans-serif;letter-spacing:.2px;}
  .front-id{left:280px;top:116px;font:200 19px/1 "Kanit",sans-serif;letter-spacing:.3px;}
  .case-text{left:280px;top:147px;font:italic 400 12px/14.3px "Mulish",sans-serif;}
  .divider{position:absolute;left:280px;top:335px;width:281px;height:2px;background:var(--white);}
  .options{left:280px;top:343px;font:600 12.2px/14.5px "Mulish",sans-serif;}

  /* Back card */
  .back-title{left:661px;top:58px;font:italic 700 19px/1 "Kanit",sans-serif;color:var(--accent);}
  .notes{left:661px;font:italic 400 9px/11px "Mulish",sans-serif;}
  .notes .label{color:var(--accent);}
  .note-def{top:84px;}
  .note-etio{top:128px;}
  .note-sym{top:183px;}
  .note-dx{top:238px;}
  .note-rx{top:325px;line-height:12px;}
  .sources{left:661px;top:378px;font:700 8.6px/1 "Tinos",serif;}
  .answer-title{left:961px;top:77px;font:italic 700 13px/1 "Kanit",sans-serif;}
  .answer-text{left:961px;top:95px;font:italic 400 10.3px/14.25px "Mulish",sans-serif;}
  .page-no{position:absolute;left:1121px;top:386px;width:16px;height:30px;background:var(--white);border-radius:8px 8px 0 0;
    font:700 11px/1 "Tinos",serif;color:var(--navy);text-align:center;padding-top:7px;}
</style>
</head>
<body>
<div class="canvas">
  <svg class="shapes" width="1200" height="436" viewBox="0 0 1200 436">
    <defs>
      <linearGradient id="frontGrad" x1="0" y1="0" x2="1" y2="0.3">
        <stop offset="0" stop-color="#e8157c"/>
        <stop offset="0.55" stop-color="#ee3f5c"/>
        <stop offset="1" stop-color="#f26a1e"/>
      </linearGradient>
      <linearGradient id="organGrad" x1="0" y1="0" x2="0" y2="1">
        <stop offset="0" stop-color="#b8543e"/>
        <stop offset="0.35" stop-color="#e0a070"/>
        <stop offset="1" stop-color="#f0cdb3"/>
      </linearGradient>
      <linearGradient id="photoGrad" x1="0" y1="0" x2="0" y2="1">
        <stop offset="0" stop-color="#dfe9f1"/>
        <stop offset="1" stop-color="#b9c9d8"/>
      </linearGradient>
      <linearGradient id="answerGrad" x1="0" y1="0" x2="1" y2="1">
        <stop offset="0" stop-color="#f26322"/>
        <stop offset="1" stop-color="#f04a4a"/>
      </linearGradient>
    </defs>

    <!-- front: organ illustration area -->
    <rect role="img" aria-label="Illustration of the human digestive organs" x="20" y="95" width="225" height="305" rx="30" fill="url(#organGrad)" opacity="0.85"/>
    <!-- front: gradient panel -->
    <path d="M143 21 H440 C520 21 590 90 592 190 L545 415 H247 C240 330 232 250 205 200 C170 130 150 70 143 21 Z" fill="url(#frontGrad)"/>
    <!-- front: portrait -->
    <circle cx="205" cy="145" r="68" fill="var(--white)"/>
    <circle role="img" aria-label="Portrait photo of a smiling doctor" cx="205" cy="145" r="63" fill="url(#photoGrad)"/>

    <!-- back: navy card -->
    <rect x="608" y="21" width="572" height="394" fill="var(--navy)"/>
    <path d="M935 21 H1180 V262 C1160 310 1110 345 1050 345 C965 345 905 290 905 215 C905 150 935 120 935 60 Z" fill="url(#answerGrad)"/>
    <path d="M608 367 C618 365 632 368 630 378 C627 388 618 392 620 402 C622 410 614 415 608 415 Z" fill="var(--orange)"/>
  </svg>

  <!-- Front of card -->
  <div class="txt front-title">Gastrointestinal</div>
  <div class="txt front-id">PATHOLOGY CASE ID 0001</div>
  <p class="txt case-text">50-year-old woman comes to the clinic because<br>she has difficulty swallowing for the past few<br>months.&nbsp; She says symptoms have been worsening.<br>She also complains of cough, mostly at night and in<br>fear of choking, has stopped eating many foods,<br>losing about 12 lbs in the past 3 months.&nbsp; Past<br>medical history is unremarkable. Vital signs are<br>normal and physical exam is unremarkable.&nbsp; Chest<br>x-ray with demonstrates an air-fluid level, while<br>manometry shows absent relaxation of the lower<br>esophageal sphincter during swallowing.&nbsp; What is<br>the most likely diagnosis?</p>
  <div class="divider"></div>
  <p class="txt options">A) GERD&nbsp; B) Barret Esophagus&nbsp; C) Achalasia<br>D) Eosinophilic esophagitis</p>

  <!-- Back of card -->
  <div class="txt back-title">Achalasia</div>
  <p class="txt notes note-def"><span class="label">Definition:</span>&nbsp; Motility disorder where esophageal<br>relaxation is impaired in the lower esophageal sphincter<br>(LES).</p>
  <p class="txt notes note-etio"><span class="label">Etiology/Pathology:</span><br>Destruction of inhibitory neurons in the Auerbach plexus.<br>Loss of peristalsis in the lower esophageal sphincter<br>(Lower-two thirds of the esophagus).</p>
  <p class="txt notes note-sym"><span class="label">P/E and Symptoms:</span> Dysphagia that is progressive,<br>regurgitation, weight-loss, dry cough, chest pain, GERD,<br>esophageal perforation, squamous cell carcinoma,<br>aspiration pneumonia.</p>
  <p class="txt notes note-dx"><span class="label">Dx:</span><br>Barium swallow will show ‘bird’s beak’ and esophageal<br>dilation.&nbsp; Manometry will present with increased resting<br>lower esophageal sphincter pressure. Endoscopy will<br>usually present with normal mucosa and LES dilation,<br>and in some cases residual material such as undigested<br>food particles may be present.</p>
  <p class="txt notes note-rx"><span class="label">Rx:</span>&nbsp; First line of treatment are nitrates, calcium channel blockers, and<br>Botulinum toxin injection in the LES.&nbsp; Long term management options<br>include esophageal dilation with pneumatic balloon and myotomy.</p>
  <div class="txt sources">Sources: Harlow’s Drug Guide | Pocket Clinical Formulary | Medireference.net | Clinibase.org</div>

  <div class="txt answer-title">C- Achalasia</div>
  <p class="txt answer-text">Symptoms and studies suggestive of<br>achalasia.&nbsp; Patient’s manometry<br>presents with no relaxation of the<br>lower esophageal sphincter during<br>swallowing. Patient also complains<br>of dysphagia and is unable to<br>swallow properly, leading to weight<br>loss.&nbsp; Patient has no past infection or<br>inflammation, ruling out eosinophilic<br>esophagitis.<br>Patient does not have chronic GERD,<br>eliminating the possibility of Barrett<br>esophagus, in which at least 5 years<br>of acid reflux are beforehand to<br>develop columnar metaplasia.</p>
  <div class="page-no">1</div>
</div>
</body>
</html>
```